Bluefield construction business cards

I need a business card with a replacement window photo or graphic on it .phone # 919 482 -7731 bluefieldconstruction@mailbox-example.com fax #919 274-8093 '' The Window Replacement Specialist"

Industry/Entity Type

Construction

```html
<!DOCTYPE html>
<html lang="en">
<head>
<meta charset="utf-8">
<title>Bluefield Construction – Business Card</title>
<link href="https://fonts.googleapis.com/css2?family=Arimo:wght@700&family=Questrial&family=Staatliches&display=swap" rel="stylesheet">
<style>
  :root {
    --backdrop: #302e2f;
    --brand-green: #6abf4b;
    --ink: #2f2f2f;
    --paper: #ffffff;
    --label: #ffffff;
  }
  * { margin: 0; padding: 0; box-sizing: border-box; }
  html, body { width: 962px; height: 1200px; overflow: hidden; }
  body {
    position: relative;
    background: var(--backdrop);
    font-family: "Questrial", sans-serif;
  }
  .side-label {
    position: absolute;
    left: 35px;
    width: 0;
    font-family: "Arimo", sans-serif;
    font-weight: 700;
    font-size: 28px;
    color: var(--label);
    white-space: nowrap;
  }
  .side-label span {
    display: block;
    transform: translate(-50%, -50%) rotate(-90deg);
    width: max-content;
  }
  .side-label--front { top: 320px; }
  .side-label--back { top: 870px; }

  .card {
    position: absolute;
    left: 73px;
    width: 816px;
    height: 477px;
  }
  .card--front { top: 86px; background: var(--brand-green); }
  .card--back { top: 636px; background: var(--paper); }

  .installer-illustration {
    position: absolute;
    left: 168px;
    top: 94px;
    width: 276px;
    height: 290px;
    border-radius: 6px;
    background: radial-gradient(circle at 45% 45%, #f2f2f2 0%, #cfd6cb 45%, #3a3a3a 100%);
    opacity: 0.85;
  }
  .tagline-stack {
    position: absolute;
    left: 441px;
    top: 228px;
    font-family: "Staatliches", sans-serif;
    font-size: 37px;
    line-height: 37px;
    color: var(--ink);
    letter-spacing: 0.5px;
  }

  .company-name {
    position: absolute;
    left: 58px;
    top: 110px;
    font-family: "Questrial", sans-serif;
    font-size: 54px;
    line-height: 1;
    color: var(--brand-green);
    display: flex;
    align-items: center;
    gap: 16px;
  }
  .company-name__mark {
    width: 40px;
    height: 40px;
    background: var(--brand-green);
  }
  .contact-list {
    position: absolute;
    left: 120px;
    top: 262px;
    font-size: 25px;
    line-height: 35px;
    color: var(--ink);
  }
  .contact-row { display: flex; }
  .contact-row dt { width: 93px; }
  .contact-row dd { white-space: nowrap; }
  .tagline-band {
    position: absolute;
    left: 0;
    top: 380px;
    width: 816px;
    height: 55px;
    background: var(--brand-green);
    font-family: "Staatliches", sans-serif;
    font-size: 35px;
    line-height: 55px;
    padding-left: 120px;
    letter-spacing: 1.5px;
    color: var(--ink);
  }
</style>
</head>
<body>
  <div class="side-label side-label--front"><span>SIDE 1</span></div>
  <div class="side-label side-label--back"><span>SIDE 2</span></div>

  <section class="card card--front">
    <div class="installer-illustration" role="img" aria-label="Cartoon illustration of a window installer in overalls leaning on a window frame in front of gears"></div>
    <p class="tagline-stack">The<br>Window<br>Replacement<br>Specialist</p>
  </section>

  <section class="card card--back">
    <div class="company-name">
      <span class="company-name__mark"></span>
      <span>Bluefield Construction</span>
    </div>
    <dl class="contact-list">
      <div class="contact-row"><dt>Phone :</dt><dd>919 482 7731</dd></div>
      <div class="contact-row"><dt>Email&nbsp;&nbsp;:</dt><dd>bluefieldconstruction@mailbox-example.com</dd></div>
      <div class="contact-row"><dt>Fax&nbsp;&nbsp;&nbsp;&nbsp;&nbsp;&nbsp;:</dt><dd>919 274 8093</dd></div>
    </dl>
    <div class="tagline-band">The Window Replacement Specialist</div>
  </section>
</body>
</html>
```